Bright Oak Fitness Facility Business Cards

Business Card Design that incorporates the logo and tagline

Target Market(s)

Fitness, People Who Exercise

Contact Information for Business Card

2817 Mossgrove Bend Road
Brookhaven, Ohio 43190
Phone: 614-555-Jump (5867)
www.brightoakfitness.example
info@brightoakfitness.example

Requirements
Must have
• Logo, Address, Website, email and tagline "Train With Purpose". Colors should be red/black/grey/white

```html
<!DOCTYPE html>
<html lang="en">
<head>
<meta charset="utf-8">
<title>Bright Oak Fitness – Business Cards</title>
<link href="https://fonts.googleapis.com/css2?family=Lato:wght@400;700&family=Oswald:wght@500&display=swap" rel="stylesheet">
<style>
  :root {
    --red: #e3202a;
    --black: #1b1b1b;
    --ink: #222222;
    --card-front: #ffffff;
    --card-back: #ececec;
    --page: #f2f2f4;
  }
  * { margin: 0; padding: 0; box-sizing: border-box; }
  html, body {
    width: 1200px; height: 1200px; overflow: hidden;
    background: var(--page);
    font-family: "Lato", sans-serif;
    color: var(--ink);
  }
  .card {
    position: absolute;
    left: 223px; width: 815px; height: 466px;
    box-shadow: 0 2px 6px rgba(0,0,0,0.12);
  }
  .card--front { top: 76px; background: var(--card-front); }
  .card--back { top: 658px; background: var(--card-back); }

  .person {
    position: absolute; left: 55px; top: 190px;
    padding-left: 20px;
    border-left: 8px solid var(--red);
    height: 60px;
  }
  .person__name {
    font-family: "Oswald", sans-serif; font-weight: 500;
    font-size: 44px; line-height: 40px; color: var(--red);
    letter-spacing: 0.5px; margin-top: -2px;
  }
  .person__role { font-size: 18px; line-height: 20px; margin-top: 3px; }

  .address {
    position: absolute; left: 56px; top: 302px;
    font-size: 17px; line-height: 21px; letter-spacing: -0.2px;
  }
  .contacts {
    position: absolute; left: 56px; top: 365px;
    list-style: none; font-size: 19px; line-height: 24.5px;
  }
  .contacts li { display: flex; align-items: center; gap: 9px; }
  .contacts svg { width: 15px; height: 15px; flex: none; }

  .brand {
    position: absolute; display: flex; align-items: center; gap: 10px;
    font-family: "Lato", sans-serif; font-weight: 700;
    color: var(--red); white-space: nowrap;
  }
  .brand__mark { background: var(--red); flex: none; }
  .card--front .brand { right: 48px; top: 112px; font-size: 32px; }
  .card--front .brand__mark { width: 22px; height: 22px; }

  .back-lockup {
    position: absolute; left: 0; right: 0; top: 180px;
    display: flex; flex-direction: column; align-items: center;
  }
  .card--back .brand { position: static; font-size: 50px; gap: 14px; }
  .card--back .brand__mark { width: 34px; height: 34px; }
  .tagline { font-size: 17px; margin-top: 14px; color: var(--black); letter-spacing: 0.2px; }
</style>
</head>
<body>

<section class="card card--front">
  <div class="brand"><span class="brand__mark"></span>BRIGHT OAK FITNESS</div>

  <div class="person">
    <div class="person__name">MARCUS HALE</div>
    <div class="person__role">MANAGER</div>
  </div>

  <p class="address">2817 Mossgrove Bend Road<br>Brookhaven, Ohio 43190</p>

  <ul class="contacts">
    <li>
      <svg viewBox="0 0 16 16" fill="none" stroke="var(--red)" stroke-width="1.6" aria-hidden="true"><path d="M3 2l3 1 1 3-2 1.5c1 2 2.5 3.5 4.5 4.5L11 10l3 1 .5 3c-6 1-12-5-11.5-12z"/></svg>
      614-555-Jump (5867)
    </li>
    <li>
      <svg viewBox="0 0 16 16" fill="none" stroke="var(--red)" stroke-width="1.4" aria-hidden="true"><rect x="1" y="3" width="14" height="10"/><path d="M1 3l7 6 7-6M1 13l5-5M15 13l-5-5"/></svg>
      info@brightoakfitness.example
    </li>
    <li>
      <svg viewBox="0 0 16 16" fill="none" stroke="var(--red)" stroke-width="1.3" aria-hidden="true"><circle cx="8" cy="8" r="6.5"/><ellipse cx="8" cy="8" rx="3" ry="6.5"/><path d="M1.5 8h13M2.5 5h11M2.5 11h11"/></svg>
      www.brightoakfitness.example
    </li>
  </ul>
</section>

<section class="card card--back">
  <div class="back-lockup">
    <div class="brand"><span class="brand__mark"></span>BRIGHT OAK FITNESS</div>
    <div class="tagline">TRAIN WITH PURPOSE</div>
  </div>
</section>

</body>
</html>
```